Better Advertisement Flyer

- On the advertisement flyer, there should be a new logo.
- As per the screenshot, the Search, Shortlist, Send, Save Buttons should be there but with a better design. The LAYOUT for the top of the flyer should be the same as the website but a change in design

Need advertisement flyer to promote directory (bridalcompass.example.sg) Uploaded is our existing flyer. REQUIRE A MUCH BETTER DESIGN

Overview of service: directory for vendors to list to their service in.
Directory will then be marketed to consumers. Main feature is the mass send
enquiry function where consumers can check off vendors and mass send their
enquiry, vendor will also receive a monthly report on how many users open
their listing. (Bridalcompass.example.sg)

Target market: for vendors to advertise in our directory

Design specifics: as per website color scheme

Contact Details to be on the flyer:
Contact Number: 6412-9076
E-mail: advertise@bridalcompass.example.sg

Please view the change in content. Also, we want to have a new look so if possible, have a new logo with the flyer. Thank you!

Target Market(s)

- Wedding Vendors for them to advertise in our directory
- Design is meant for Print Advertisement

Industry/Entity Type

It Service

Font styles to use
Serif

Colors
f9d9e8
d0ebe7
fff3d1

Requirements
Must have

• A Different Logo to Match the flyer. Logo must be Eye-Catching, different (like a magazine cover logo)

Content

Advertiser Benefits

(1) Increase Your Exposure
(2) Enquires Directed Straight To Your Inbox
(3) Featured Advertorial Post
(4) Online Reputation Management
(5) List Your Upcoming Events
(6) Advertise Your Promotions
(7) List in Multiple Categories

About The Bridal Compass

A Revolutionary online platform developed for brides who want instant contact with every Wedding Vendor in just one e-mail,

The Bridal Compass has a simple, clean and easy to use interface that lets consumers choose and mass send their enquiries!

Get potential customers in the fastest way and boost your sales revenue today!

Simple Steps To Using The Bridal Compass (Please use boxes like that of the website)
(1) Find Wedding Services using the Wedding Directory
(2) Create a list of businesses that you would like to contact
(3) Send an enquiry to multiple businesses at the same time
(4) Save Time & Money Using Wedding Deals

(Put the Email Envelope) advertise@bridalcompass.example.sg
W: bridalcompass.example.sg
Nice to have
• Color: As per the website / current colour. ( No Strong Colors) Use lesser pink and more neutral colours like green & yellow tone as per the colour palette
Open to changes but the must have colour is the green on the Website

```html
<!DOCTYPE html>
<html lang="en">
<head>
<meta charset="utf-8">
<title>The Bridal Compass – Advertiser Flyer</title>
<link rel="stylesheet" href="https://fonts.googleapis.com/css2?family=Playfair+Display:wght@700;900&family=Libre+Baskerville&family=Arimo:wght@400;700&family=Roboto+Condensed:wght@700&family=Parisienne&display=swap">
<style>
  :root {
    --page: #d6d6d6;
    --mint: #d4ecea;
    --mint-deep: #b9e3d8;
    --cream: #fff6d3;
    --teal: #5fc2b2;
    --pink: #e98bb5;
    --pink-soft: #f9d9e8;
    --lavender: #c8caee;
    --ink: #1f1f1f;
    --white: #ffffff;
  }
  * { box-sizing: border-box; margin: 0; padding: 0; }
  html, body { width: 1200px; height: 1000px; overflow: hidden; background: var(--page); }
  .flyer {
    position: absolute; left: 282px; top: 88px; width: 636px; height: 824px;
    background: var(--mint); overflow: hidden;
    font-family: "Arimo", Arial, sans-serif; color: var(--ink);
  }
  .flyer-backdrop { position: absolute; inset: 0; }
  .abs { position: absolute; }

  /* masthead */
  .masthead {
    left: 0; top: 40px; width: 636px; height: 62px;
    display: flex; align-items: center; justify-content: center; gap: 10px;
  }
  .masthead-mark { width: 20px; height: 20px; border-radius: 50%; background: var(--teal); flex: none; }
  .masthead-name {
    font: 900 52px/1 "Playfair Display", serif; color: var(--teal); letter-spacing: -0.5px; white-space: nowrap;
  }
  .tagline-ribbon { left: 48px; top: 104px; width: 542px; height: 44px; }
  .tagline {
    left: 51px; top: 114px; width: 536px; text-align: center;
    font: 400 18.5px "Arimo", Arial, sans-serif; color: var(--ink);
  }
  .swirl-decor {
    left: 380px; top: 148px; width: 220px; height: 62px; border-radius: 40px 40px 0 0;
    background: radial-gradient(ellipse at center, #c4e6e1 0%, rgba(196,230,225,0) 75%);
  }

  /* benefits */
  .benefits-title {
    left: 26px; top: 188px; font: 700 25px "Roboto Condensed", sans-serif; letter-spacing: -0.3px;
  }
  .benefit-list { left: 0; top: 220px; list-style: none; }
  .benefit {
    width: 290px; height: 21px; margin-bottom: 7px; padding-left: 26px;
    border-radius: 0 11px 11px 0; white-space: nowrap;
    font: 400 11.5px/21px "Libre Baskerville", serif; color: #333;
  }
  .benefit:nth-child(odd) { background: var(--lavender); }
  .benefit:nth-child(even) { background: var(--mint-deep); }
  .benefits-note {
    left: 26px; top: 417px; width: 212px; font: 400 12.5px/16px "Arimo", Arial, sans-serif;
  }

  /* about */
  .about-title {
    left: 305px; width: 300px; top: 222px; text-align: center; white-space: nowrap;
    font: 400 25px "Parisienne", cursive; color: var(--pink);
  }
  .about-copy {
    left: 315px; width: 282px; top: 253px; text-align: center;
    font: 400 16px/20px "Arimo", Arial, sans-serif;
  }
  .skyrocket {
    left: 289px; top: 350px; width: 208px; height: 54px; background: var(--mint);
    padding: 3px 6px; font: 400 15px/18px "Libre Baskerville", serif; white-space: nowrap;
  }
  .skyrocket strong { font: 900 25px/30px "Playfair Display", serif; color: var(--pink); }
  .skyrocket b { font: 700 21px "Playfair Display", serif; }
  .sales-chart { left: 300px; top: 355px; width: 310px; height: 135px; }

  /* steps */
  .steps-title {
    left: 232px; top: 508px; font: 700 18px "Playfair Display", serif; color: var(--teal); white-space: nowrap;
  }
  .step-row { left: 232px; top: 538px; display: flex; gap: 7px; }
  .step {
    width: 91px; height: 161px; background: var(--mint); border: 4px solid var(--white);
    box-shadow: 0 3px 5px rgba(0,0,0,0.22); text-align: center; padding-top: 6px;
  }
  .step-name { font: 700 14px "Playfair Display", serif; color: var(--pink); letter-spacing: 0.3px; }
  .step-icon { display: block; margin: 6px auto 4px; width: 46px; height: 46px; }
  .step-text { font: 400 12px/14.5px "Arimo", Arial, sans-serif; padding: 0 3px; }

  .tablet-visual {
    left: 4px; top: 545px; width: 200px; height: 150px; border-radius: 12px;
    background: linear-gradient(135deg, #2b2b2b 0%, #444 45%, #e9d6c8 100%);
    transform: rotate(-4deg);
  }
  .bouquet-visual {
    left: 103px; top: 495px; width: 118px; height: 118px; border-radius: 50%;
    border: 3px solid var(--white);
    background: radial-gradient(circle at 45% 40%, #ffffff 0%, #f1efe8 50%, #b9927a 100%);
  }

  /* contact */
  .contact-line {
    left: 0; width: 636px; top: 735px; display: flex; align-items: center; justify-content: center; gap: 6px;
    font: 400 15px "Arimo", Arial, sans-serif; color: #333; white-space: nowrap;
  }
  .contact-line strong { font: 700 17px "Arimo", Arial, sans-serif; color: var(--ink); }
  .contact-sep { color: var(--teal); }
  .mail-icon { width: 20px; height: 14px; flex: none; }
  .site-pill {
    left: 138px; top: 765px; width: 360px; height: 42px; border-radius: 9px;
    background: var(--pink); border: 3px solid #f3b9d2; color: var(--white);
    text-align: center; font: 700 23px/36px "Arimo", Arial, sans-serif;
  }
</style>
</head>
<body>
<main class="flyer">
  <svg class="flyer-backdrop" width="636" height="824" viewBox="0 0 636 824" aria-hidden="true">
    <path d="M0,178 C110,160 210,158 320,190 C430,222 540,214 636,182 L636,500 L0,500 Z" fill="var(--cream)"/>
    <path d="M0,505 C90,480 170,482 270,500 C380,520 520,520 636,494 L636,724 L0,724 Z" fill="var(--mint)"/>
    <path d="M0,500 L636,500 L636,494 C520,520 380,520 270,500 C170,482 90,480 0,505 Z" fill="var(--cream)"/>
    <rect x="0" y="724" width="636" height="100" fill="var(--cream)"/>
  </svg>

  <div class="abs swirl-decor" role="img" aria-label="Soft decorative swirl pattern"></div>

  <header>
    <div class="abs masthead">
      <span class="masthead-mark"></span>
      <h1 class="masthead-name">The Bridal Compass</h1>
    </div>
    <svg class="abs tagline-ribbon" viewBox="0 0 542 44" aria-hidden="true">
      <polygon points="0,6 18,6 10,22 18,38 0,38 8,22" fill="var(--teal)"/>
      <polygon points="542,6 524,6 532,22 524,38 542,38 534,22" fill="var(--teal)"/>
      <rect x="12" y="4" width="518" height="36" fill="var(--pink-soft)" stroke="var(--teal)" stroke-width="2"/>
    </svg>
    <p class="abs tagline">The Fastest Way To Find Wedding Services in Singapore</p>
  </header>

  <section>
    <h2 class="abs benefits-title">ADVERTISER BENEFITS</h2>
    <ul class="abs benefit-list">
      <li class="benefit">Increase Your Exposure</li>
      <li class="benefit">Enquires Directed Straight To Your Inbox</li>
      <li class="benefit">Featured Advertorial Post</li>
      <li class="benefit">Online Reputation Management</li>
      <li class="benefit">List Your Upcoming Events</li>
      <li class="benefit">Advertise Your Promotions</li>
      <li class="benefit">List in Multiple Categories</li>
    </ul>
    <p class="abs benefits-note">The Bridal Compass has a simple, clean and easy to use interface that lets consumers choose and mass send their enquiries!</p>
  </section>

  <section>
    <h2 class="abs about-title">About The Bridal Compass</h2>
    <p class="abs about-copy">A Revolutionary online platform developed for brides who want instant contact with every wedding vendor in just one email</p>
    <svg class="abs sales-chart" viewBox="0 0 310 135" aria-hidden="true">
      <g fill="var(--teal)">
        <rect x="3" y="123" width="28" height="9"/>
        <rect x="50" y="117" width="28" height="15"/>
        <rect x="96" y="109" width="28" height="23"/>
        <rect x="142" y="100" width="28" height="32"/>
        <rect x="188" y="89" width="28" height="43"/>
        <rect x="230" y="74" width="28" height="58"/>
        <rect x="276" y="52" width="28" height="80"/>
      </g>
      <path d="M8,110 C90,90 190,80 268,20" fill="none" stroke="var(--pink)" stroke-width="6" stroke-linecap="round"/>
      <polygon points="286,6 256,14 276,34" fill="var(--pink)"/>
      <text x="8" y="104" transform="rotate(-13 8 104)" font-family="Arimo, Arial, sans-serif" font-size="17" fill="var(--ink)">Boost Your Sales</text>
    </svg>
    <p class="abs skyrocket">Watch as your business<br><strong>Skyrocket</strong> <b>today!</b></p>
  </section>

  <section>
    <div class="abs tablet-visual" role="img" aria-label="Hand tapping a tablet showing the directory website"></div>
    <div class="abs bouquet-visual" role="img" aria-label="White rose bridal bouquet"></div>
    <h2 class="abs steps-title">Simple Steps To Using The Bridal Compass</h2>
    <div class="abs step-row">
      <div class="step">
        <p class="step-name">SEARCH</p>
        <svg class="step-icon" viewBox="0 0 46 46" aria-hidden="true">
          <circle cx="22" cy="16" r="11" fill="none" stroke="var(--teal)" stroke-width="4"/>
          <rect x="20" y="27" width="4" height="16" rx="2" fill="var(--teal)"/>
        </svg>
        <p class="step-text">Find wedding services using the wedding directory</p>
      </div>
      <div class="step">
        <p class="step-name">SHORTLIST</p>
        <svg class="step-icon" viewBox="0 0 46 46" aria-hidden="true">
          <rect x="6" y="8" width="34" height="34" fill="none" stroke="var(--teal)" stroke-width="3"/>
          <path d="M13,24 L21,33 L40,6" fill="none" stroke="var(--pink)" stroke-width="4" stroke-linecap="round" stroke-linejoin="round"/>
        </svg>
        <p class="step-text">Create a list of businesses you would like to contact</p>
      </div>
      <div class="step">
        <p class="step-name">SEND</p>
        <svg class="step-icon" viewBox="0 0 46 46" aria-hidden="true">
          <rect x="3" y="10" width="40" height="28" fill="var(--teal)"/>
          <path d="M3,10 L23,27 L43,10" fill="none" stroke="var(--white)" stroke-width="2"/>
          <circle cx="23" cy="24" r="4" fill="var(--pink)"/>
        </svg>
        <p class="step-text">Send an enquiry to multiple businesses at the same time</p>
      </div>
      <div class="step">
        <p class="step-name">SAVE</p>
        <svg class="step-icon" viewBox="0 0 46 46" aria-hidden="true">
          <circle cx="23" cy="29" r="14" fill="var(--teal)"/>
          <rect x="18" y="5" width="10" height="10" rx="2" fill="var(--teal)"/>
          <text x="23" y="35" text-anchor="middle" font-family="Arimo, Arial, sans-serif" font-weight="700" font-size="16" fill="var(--pink)">$</text>
        </svg>
        <p class="step-text">Save time &amp; money using Wedding Deals</p>
      </div>
    </div>
  </section>

  <footer>
    <p class="abs contact-line">
      To Find Out More: <strong>6412-9076</strong>
      <span class="contact-sep">|</span>
      <svg class="mail-icon" viewBox="0 0 20 14" aria-hidden="true">
        <rect x="0.5" y="0.5" width="19" height="13" fill="var(--teal)"/>
        <path d="M0.5,0.5 L10,8 L19.5,0.5" fill="none" stroke="var(--white)" stroke-width="1.5"/>
      </svg>
      <strong>advertise@bridalcompass.example.sg</strong>
    </p>
    <p class="abs site-pill">bridalcompass.example.sg</p>
  </footer>
</main>
</body>
</html>
```